Design for Certificate

Design a certificate for training, providing our company logo such as attachments. Company's name is "ØSTRA Velmark Advisory Ltd", please refer to our company profile: https://www.ostra-velmark.example/company_info

The style of the current certificate is also attached, and another certificate of another company can be referred to. Psd & jpg are required for the final draft (the layers of psd are not merged). Thanks!

```html
<!DOCTYPE html>
<html lang="en">
<head>
<meta charset="utf-8">
<title>Certificate of Completion – ØSTRA Velmark Advisory Ltd</title>
<link rel="stylesheet" href="https://fonts.googleapis.com/css2?family=Montserrat:wght@400;500;600&family=Great+Vibes&display=swap">
<style>
  :root {
    --paper: #fdfcf8;
    --paper-tint: #f7f3e8;
    --gold: #b3973f;
    --gold-frame: #c5aa66;
    --accent: #e8a46d;
    --seal: #243033;
    --seal-text: #e3b899;
  }
  * { margin: 0; padding: 0; box-sizing: border-box; }
  html, body { width: 1200px; height: 873px; overflow: hidden; background: var(--paper); }
  .certificate {
    position: relative;
    width: 1200px;
    height: 873px;
    font-family: "Montserrat", sans-serif;
    color: var(--gold);
  }
  .certificate__backdrop {
    position: absolute;
    inset: 0;
    background: linear-gradient(135deg, var(--paper) 0%, var(--paper-tint) 50%, var(--paper) 100%);
  }
  .certificate__frame {
    position: absolute;
    left: 26px; top: 24px;
    width: 1148px; height: 825px;
    border: 6px solid var(--gold-frame);
  }
  .center-text {
    position: absolute;
    left: 0; right: 0;
    text-align: center;
    white-space: nowrap;
  }
  .title {
    position: absolute;
    left: 0; right: 0;
    top: 68px;
    text-align: center;
    font-family: "Great Vibes", cursive;
    font-size: 150px;
    line-height: 1;
    color: var(--gold);
  }
  .subtitle {
    position: absolute;
    left: 608px; top: 220px;
    font-size: 25px;
    letter-spacing: 1.5px;
  }
  .awarded {
    top: 331px;
    font-size: 31px;
    letter-spacing: 4px;
  }
  .name-line {
    position: absolute;
    left: 181px; top: 481px;
    width: 836px; height: 2px;
    background: var(--gold);
  }
  .completed {
    top: 520px;
    font-size: 24px;
    letter-spacing: 3px;
  }
  .course {
    top: 600px;
    left: 155px; right: auto;
    width: 873px;
    font-size: 28px;
    letter-spacing: 2.4px;
  }
  .course__name { color: var(--accent); font-weight: 600; }
  .seal {
    position: absolute;
    left: 479px; top: 671px;
    width: 144px; height: 144px;
    border-radius: 50%;
    background: var(--seal);
    display: flex;
    align-items: center;
    justify-content: center;
  }
  .seal__name {
    font-family: "Montserrat", sans-serif;
    font-weight: 500;
    font-size: 26px;
    letter-spacing: 2px;
    color: var(--seal-text);
  }
  .sign {
    position: absolute;
    top: 741px;
    text-align: center;
  }
  .sign__line { height: 2px; background: var(--gold); }
  .sign__label {
    margin-top: 16px;
    font-size: 22px;
    letter-spacing: 1.5px;
    white-space: nowrap;
  }
  .sign--number { left: 198px; width: 206px; }
  .sign--officer { left: 691px; width: 332px; }
</style>
</head>
<body>
  <main class="certificate">
    <div class="certificate__backdrop" role="img" aria-label="Soft cream background with a faint geometric line pattern"></div>
    <div class="certificate__frame"></div>

    <h1 class="title">Certificate</h1>
    <p class="subtitle">OF COMPLETION</p>

    <p class="center-text awarded">THIS CERTIFICATE IS AWARDED TO</p>
    <div class="name-line"></div>

    <p class="center-text completed">HAS SUCCESSFULLY COMPLETED</p>
    <p class="center-text course"><span class="course__name">BRAND REPUTATION MANAGEMENT</span> TRAINING COURSE</p>

    <div class="sign sign--number">
      <div class="sign__line"></div>
      <p class="sign__label">Certificate No</p>
    </div>

    <div class="seal">
      <span class="seal__name">ØSTRA</span>
    </div>

    <div class="sign sign--officer">
      <div class="sign__line"></div>
      <p class="sign__label">Chief Technology Officer</p>
    </div>
  </main>
</body>
</html>
```